Business Card Admin Services

I have just selected a new logo. Now I need a business card.

The business is contract administrative services. We provide high value administrative services to small businesses/offices. We are professional, efficient, but also have fun and energetic personalities.

Olive Parker
Olive@OfficeFalcon.ca
604-319-4870
OfficeFalcon.ca

I will also want Friendbook, Chirper and WorkLink icons on the card - please up my "handles" beside each.
Friendbook is OfficeFalconCanada
Chirper is @OFalconOlive
WorkLink is OliveParkerOfficeFalcon
Updates

New logo just updated.  Thanks for your patience!

Target Market(s)

Small businesses, professional offices

Industry/Entity Type

Business

Requirements
Must have
• bold, fun use of my colours
font needs to be consistent with the logo
Nice to have
• I quite like a closeup of the head

```html
<!DOCTYPE html>
<html lang="en">
<head>
<meta charset="utf-8">
<title>Office Falcon – Business Card</title>
<link href="https://fonts.googleapis.com/css2?family=Barlow:wght@400;500&family=Raleway:wght@400&display=swap" rel="stylesheet">
<style>
  :root {
    --backdrop: #e4e4e4;
    --card-white: #ffffff;
    --brand-magenta: #dc117a;
    --brand-magenta-deep: #6e0a3c;
    --ink: #2a1020;
    --logo-ink: #222222;
    --tab-white: #ffffff;
  }
  html, body {
    margin: 0;
    padding: 0;
    width: 1200px;
    height: 681px;
    overflow: hidden;
    background: var(--backdrop);
  }
  .canvas {
    position: relative;
    width: 1200px;
    height: 681px;
  }
  .business-card {
    position: absolute;
    left: 203px;
    top: 117px;
    width: 793px;
    height: 447px;
    background: var(--brand-magenta);
    overflow: hidden;
    box-shadow: 0 0 0 1px rgba(0,0,0,0.35);
  }
  .brand-panel {
    position: absolute;
    left: 0;
    top: 0;
    width: 222px;
    height: 100%;
    background: var(--card-white);
  }
  .brand-mark {
    position: absolute;
    left: 37px;
    top: 177px;
    width: 94px;
    height: 94px;
    border-radius: 50%;
    background: var(--brand-magenta);
  }
  .brand-name {
    position: absolute;
    left: 181px;
    top: 222px;
    transform: translate(-50%, -50%) rotate(-90deg);
    white-space: nowrap;
    font-family: "Raleway", sans-serif;
    font-weight: 400;
    font-size: 35px;
    letter-spacing: 1px;
    color: var(--logo-ink);
    line-height: 1;
  }
  .panel-fold {
    position: absolute;
    left: 222px;
    top: 0;
    width: 34px;
    height: 100%;
    background: linear-gradient(to right, rgba(70,5,40,0.75), rgba(120,8,65,0.25) 45%, rgba(220,17,122,0) 100%);
    -webkit-mask: linear-gradient(to bottom, transparent 0%, #000 12%, #000 88%, transparent 100%);
            mask: linear-gradient(to bottom, transparent 0%, #000 12%, #000 88%, transparent 100%);
  }
  .social-row {
    position: absolute;
    right: 28px;
    top: 46px;
    display: flex;
    gap: 16px;
    font-family: "Barlow", sans-serif;
    font-weight: 500;
    font-size: 15px;
    color: var(--card-white);
  }
  .social-item {
    display: flex;
    align-items: center;
    gap: 6px;
  }
  .social-item::before {
    content: "";
    width: 12px;
    height: 12px;
    background: var(--card-white);
  }
  .contact-list {
    position: absolute;
    right: 82px;
    top: 180px;
    margin: 0;
    padding: 0;
    list-style: none;
    text-align: right;
    font-family: "Barlow", sans-serif;
    font-weight: 500;
    font-size: 21px;
    letter-spacing: 0.6px;
    color: var(--ink);
  }
  .contact-list li {
    height: 38px;
    line-height: 38px;
  }
  .icon-tab {
    position: absolute;
    left: 723px;
    top: 175px;
    width: 80px;
    height: 247px;
    background: var(--tab-white);
    border-radius: 8px;
  }
  .contact-icon {
    position: absolute;
    left: 13px;
    width: 22px;
    height: 22px;
  }
  .contact-icon * {
    fill: none;
    stroke: var(--brand-magenta);
    stroke-width: 1.8;
    stroke-linecap: round;
    stroke-linejoin: round;
  }
  .contact-icon .solid { fill: var(--brand-magenta); stroke: none; }
</style>
</head>
<body>
<main class="canvas">
  <section class="business-card">
    <div class="brand-panel">
      <div class="brand-mark" role="img" aria-label="Office Falcon mascot character in a magenta circle"></div>
      <div class="brand-name">OFFICE FALCON</div>
    </div>
    <div class="panel-fold"></div>

    <div class="social-row">
      <span class="social-item">Friendbook</span>
      <span class="social-item">Chirper</span>
      <span class="social-item">WorkLink</span>
    </div>

    <ul class="contact-list">
      <li>Your residential or commercial</li>
      <li>or office address</li>
      <li>(00) 00 00000</li>
      <li>(00) 00000000</li>
      <li>info.support@yourwebsite.com</li>
      <li>www.yourwebsite.com</li>
    </ul>

    <div class="icon-tab">
      <svg class="contact-icon" style="top:18px" viewBox="0 0 22 22" aria-hidden="true">
        <path class="solid" d="M11 1.5a6.5 6.5 0 0 0-6.5 6.5c0 4.8 6.5 12.5 6.5 12.5s6.5-7.7 6.5-12.5A6.5 6.5 0 0 0 11 1.5zm0 9a2.5 2.5 0 1 1 0-5 2.5 2.5 0 0 1 0 5z"/>
      </svg>
      <svg class="contact-icon" style="top:90px" viewBox="0 0 22 22" aria-hidden="true">
        <path d="M5 3l3 0 1.5 4-2 1.5a10 10 0 0 0 5 5l1.5-2 4 1.5 0 3a2 2 0 0 1-2 2A15 15 0 0 1 3 5a2 2 0 0 1 2-2z"/>
        <path d="M14 3.5a5 5 0 0 1 4.5 4.5M14 6.5a2 2 0 0 1 1.5 1.5"/>
      </svg>
      <svg class="contact-icon" style="top:127px" viewBox="0 0 22 22" aria-hidden="true">
        <rect x="6" y="1.5" width="10" height="19" rx="1.8"/>
        <path d="M8 4.5h6v11H8zM10.5 18h1"/>
      </svg>
      <svg class="contact-icon" style="top:165px" viewBox="0 0 22 22" aria-hidden="true">
        <rect x="1.5" y="4.5" width="19" height="13"/>
        <path d="M1.5 4.5l9.5 8 9.5-8M1.5 17.5l7-6M20.5 17.5l-7-6"/>
      </svg>
      <svg class="contact-icon" style="top:203px" viewBox="0 0 22 22" aria-hidden="true">
        <circle cx="11" cy="11" r="9"/>
        <ellipse cx="11" cy="11" rx="4" ry="9"/>
        <path d="M2 11h18M3.5 6h15M3.5 16h15"/>
      </svg>
    </div>
  </section>
</main>
</body>
</html>
```